Modern, traditional Catering Menu for hotel and conference centre

Modernization of Catering menu while still making this very legible and clear to all guests. Template required in Microsoft word document so that updates to menu items can be easily updated. Menu needs style relatable to hotel and conference centre in an area known for apples, farming and awe-inspiring landscape.

Target Market(s)

Conference and meeting groups,

Industry/Entity Type

Hospitality

Font styles to use
Serif
Script

Colors

Designer to choose colors to be used in the design.

Requirements
Must have
• Legible and clear headers and modern look.
• Microsoft word template to easily be able to make updates.
Nice to have
• Something unique related to apples and our logo

```html
<!DOCTYPE html>
<html lang="en">
<head>
<meta charset="utf-8">
<title>Maple Hollow Inn – Our Facility</title>
<link rel="stylesheet" href="https://fonts.googleapis.com/css2?family=Tinos:ital,wght@0,400;0,700;1,400;1,700&family=Crimson+Text:wght@400;600&display=swap">
<style>
  :root {
    --backdrop: #e4e5e6;
    --paper: #ffffff;
    --ink: #111111;
    --brand-ink: #2b0d0d;
    --muted: #7a7a7a;
    --teal-light: #00948f;
    --teal-dark: #03646f;
    --copper: #c0762a;
    --rule: #222222;
  }
  * { margin: 0; padding: 0; box-sizing: border-box; }
  html, body { width: 1200px; height: 1200px; overflow: hidden; background: var(--backdrop); }
  .page {
    position: absolute; left: 126px; top: 0;
    width: 900px; height: 1140px;
    background: var(--paper);
    transform: scale(1.0526); transform-origin: top left;
    font-family: "Tinos", "Times New Roman", serif;
    color: var(--ink);
    overflow: hidden;
  }
  .header-band {
    position: absolute; left: 0; top: 0; width: 900px; height: 96px;
    background: linear-gradient(90deg, var(--teal-light) 0%, var(--teal-dark) 50%, var(--copper) 100%);
  }
  .brand {
    position: absolute; left: 357px; width: 400px; top: 108px;
    text-align: center; font-family: "Crimson Text", serif; color: var(--brand-ink);
  }
  .brand-name { font-size: 50px; font-weight: 600; line-height: 1; }
  .brand-tagline { font-size: 14.5px; font-weight: 400; margin-top: 12px; white-space: nowrap; }
  .section-title {
    position: absolute; top: 214px; left: 0; width: 900px;
    text-align: center; font-size: 25px; font-weight: 700;
  }
  .intro {
    position: absolute; top: 262px; left: 50px; width: 780px;
    font-size: 13.8px; line-height: 16.6px;
  }
  .essentials-title {
    position: absolute; top: 342px; left: 50px; width: 800px;
    font-size: 22px; font-weight: 700; font-style: italic;
    padding-bottom: 4px; border-bottom: 1px solid var(--rule);
  }
  .essentials-list {
    position: absolute; top: 389px; left: 103px; list-style: none;
    font-size: 13.6px;
  }
  .essentials-list li { height: 31px; line-height: 18px; }
  .footer {
    position: absolute; top: 1064px; left: 66px; width: 768px;
    border-top: 1px solid #8a8a8a; padding-top: 13px;
    text-align: center; font-family: "Crimson Text", serif;
    font-size: 12.3px; line-height: 16px; color: var(--muted);
  }
  .footer .gap { display: inline-block; width: 22px; }
</style>
</head>
<body>
  <main class="page">
    <div class="header-band" role="img" aria-label="Decorative header band in teal and copper tones"></div>

    <header class="brand">
      <div class="brand-name">Maple Hollow Inn</div>
      <div class="brand-tagline">Hotel &amp; Conference Centre | Conference Groups Cider Hall</div>
    </header>

    <h1 class="section-title">Our Facility</h1>

    <p class="intro"><strong>Maple Hollow Inn</strong> is truly a landmark of hospitality in the Annapolis Valley of Nova Scotia with 101 Guest Rooms, 29 Seasonal Cabins (May - October) and Conference &amp; Event Centre with over 11,000 sq ft since established in 1972. The grounds sit nestled in one of the many beautiful apple orchards of Applebrook. Maple Hollow Inn overlooks rolling landscapes of Cape Blomidon and the Minas Basin; part of the Bay of Fundy, featuring the world famous highest tides: <em>truly an awe-inspiring view</em>.</p>

    <h2 class="essentials-title">Essentials for your event</h2>

    <ul class="essentials-list">
      <li>Professional Conference Centre</li>
      <li>Heritage Barn, a unique venue onsite offering limited catering</li>
      <li>Free parking</li>
      <li>Complimentary high-speed wireless internet</li>
      <li>Many popular attractions close by including several local wineries</li>
      <li>Parlour guestroom upgrade available to organizers and wedding couples</li>
      <li>Complimentary consultation with one of our Sales Team</li>
      <li>Menu tasting for two with our Chef for a nominal fee</li>
      <li>Guest rooms at a group rate (dependent on number of rooms rented for the occasion)</li>
      <li>Able to accommodate most dietary requirements, please inquire</li>
      <li>Children’s menus available</li>
      <li>Podium &amp; microphone available</li>
      <li>Guest book table, cake table, gift table</li>
      <li>Dance floor available at most venues</li>
      <li>Complimentary bar service (dependent on minimum sales)</li>
      <li>Complimentary cake cutting service, cake knife</li>
      <li>A selection of vases with votive candles for guest tables for a nominal rental fee</li>
      <li>White linen tablecloths and napkins</li>
      <li>Access to the breathtaking grounds for wedding photographs</li>
      <li>Seasonal fireside dining with a year round spectacular view of Cape Blomidon</li>
      <li>Windfall Quiet Lounge</li>
    </ul>

    <footer class="footer">
      <div>Exit 9, Highway 40, 210 Harvest Road South, Applebrook, Nova Scotia, B0P 1K0</div>
      <div>T: (555) 014 2290<span class="gap"></span>TF: 1 800 555 0147<span class="gap"></span>F: (555) 014 2291</div>
      <div>Effective: January 1, 2019. All prices are plus 16% gratuity plus applicable taxes and are subject to change.</div>
    </footer>
  </main>
</body>
</html>
```